Kettle Ledger Business Card design

We need a stand out business card design for Accounting practice based in Australia specialising in pubs, clubs and hotels. We help venues maximise margins, create time and manage cashflow. One club we have been working with for the last 6 months has increased revenue by 3% and margin by 5% in this time frame. We have a back office outsourced system that costs less than having a full time employee and also allows the venues the added benefit of:<br/>-using the office space to become a revenue generating opportunity. <br/>-a complete system to enhance governance, accountability and efficiency within their operation<br/>-52 weeks cover so no hassle to cover annual/sick .. leave<br/><br/>We would like to see designs that use the colours of our logo (green & blue).
Target Market(s)
Australian Pubs, Clubs & Hotels abookkeeping, accounting and tax services
Industry/Entity Type
Accountant
Contact Information for Business Card
Miriam Oakley CPA
Principal
Accountant Tax Agent
Miriam@KettleLedger-example.com.au
0418693142
www.kettleledger-example.com.au
Accounting / Payroll / Tax / SMSF / Technology
Colors
Designer to choose colors to be used in the design.
Look and feel
Each slider illustrates characteristics of the customer's brand and the style your logo design should communicate.

```html
<!DOCTYPE html>
<html lang="en">
<head>
<meta charset="utf-8">
<title>Kettle Ledger – Business Card</title>
<link href="https://fonts.googleapis.com/css2?family=Lato:wght@400;700;900&display=swap" rel="stylesheet">
<style>
  :root {
    --brand-blue: #23449b;
    --brand-green: #1f7a3a;
    --card-white: #ffffff;
    --ink: #2b2b2b;
    --stage: #e6e8ec;
  }
  * { box-sizing: border-box; margin: 0; padding: 0; }
  html, body { width: 1200px; height: 766px; overflow: hidden; }
  body {
    background: var(--stage);
    font-family: "Lato", Arial, sans-serif;
    display: flex;
    align-items: center;
    justify-content: center;
    gap: 40px;
  }
  .card {
    width: 520px;
    height: 297px;
    position: relative;
    box-shadow: 0 6px 18px rgba(0,0,0,0.18);
    overflow: hidden;
  }
  .card--front { background: var(--card-white); }
  .brand {
    position: absolute;
    left: 34px;
    top: 104px;
    width: 200px;
    display: flex;
    align-items: center;
    gap: 10px;
  }
  .brand__dot {
    width: 26px; height: 26px;
    border-radius: 50%;
    background: var(--brand-green);
    flex: none;
  }
  .brand__name {
    font-weight: 900;
    font-size: 25px;
    line-height: 1.05;
    color: var(--brand-blue);
  }
  .divider {
    position: absolute;
    left: 250px;
    top: 48px;
    width: 1.5px;
    height: 160px;
    background: var(--brand-green);
  }
  .contact {
    position: absolute;
    left: 272px;
    top: 58px;
    color: var(--ink);
  }
  .contact__name {
    font-weight: 700;
    font-size: 18px;
    color: var(--brand-blue);
  }
  .contact__role {
    font-weight: 700;
    font-size: 12.5px;
    color: var(--brand-green);
    margin-top: 2px;
  }
  .contact__title { font-size: 12px; margin-top: 2px; }
  .contact__list { list-style: none; margin-top: 14px; }
  .contact__item {
    display: flex; align-items: center; gap: 6px;
    font-size: 11.5px; line-height: 1.6;
  }
  .contact__icon { width: 10px; height: 10px; flex: none; color: var(--brand-blue); }
  .services {
    position: absolute;
    left: 0; right: 0; bottom: 0;
    height: 40px;
    background: var(--brand-blue);
    display: flex; align-items: center; justify-content: center;
    gap: 9px;
    color: #fff;
    font-size: 11.5px;
    letter-spacing: 0.8px;
    text-transform: uppercase;
  }
  .services__sep {
    width: 5px; height: 5px; border-radius: 50%;
    background: #3aa655;
  }
  .card--back {
    background: linear-gradient(135deg, #2a4ca6 0%, var(--brand-blue) 55%, #3d5ab0 100%);
  }
  .pattern-area { position: absolute; inset: 0; }
</style>
</head>
<body>
  <section class="card card--front">
    <div class="brand">
      <span class="brand__dot"></span>
      <span class="brand__name">Kettle Ledger</span>
    </div>
    <div class="divider"></div>
    <div class="contact">
      <p class="contact__name">Miriam Oakley CPA</p>
      <p class="contact__role">Principal</p>
      <p class="contact__title">Accountant Tax Agent</p>
      <ul class="contact__list">
        <li class="contact__item">
          <svg class="contact__icon" viewBox="0 0 10 10"><path d="M2 0.5 L3.6 2.6 L2.7 3.6 Q3.6 5.8 6.4 7.3 L7.4 6.4 L9.5 8 L8.4 9.5 Q3 8.5 0.5 1.6 Z" fill="currentColor"/></svg>
          <span>0418693142</span>
        </li>
        <li class="contact__item">
          <svg class="contact__icon" viewBox="0 0 10 10"><rect x="0.5" y="2" width="9" height="6" fill="currentColor"/><path d="M0.5 2 L5 5.5 L9.5 2" stroke="#fff" stroke-width="0.9" fill="none"/></svg>
          <span>Miriam@KettleLedger-example.com.au</span>
        </li>
        <li class="contact__item">
          <svg class="contact__icon" viewBox="0 0 10 10"><circle cx="5" cy="5" r="4.5" fill="currentColor"/><g stroke="#fff" stroke-width="0.6" fill="none"><ellipse cx="5" cy="5" rx="2" ry="4.5"/><line x1="0.5" y1="5" x2="9.5" y2="5"/><line x1="1.3" y1="2.8" x2="8.7" y2="2.8"/><line x1="1.3" y1="7.2" x2="8.7" y2="7.2"/></g></svg>
          <span>www.kettleledger-example.com.au</span>
        </li>
      </ul>
    </div>
    <div class="services">
      <span>Accounting</span><span class="services__sep"></span>
      <span>Payroll</span><span class="services__sep"></span>
      <span>Tax</span><span class="services__sep"></span>
      <span>SMSF</span><span class="services__sep"></span>
      <span>Technology</span>
    </div>
  </section>

  <section class="card card--back">
    <div class="pattern-area" role="img" aria-label="Repeating pattern of white outlined brand symbols fading across a blue background"></div>
  </section>
</body>
</html>
```